Northern Horizons Published Photographer Website

I need a website to feature a home page slide show of 6 of my top photos then a few simple pages including; gallery, bio, social, checkout, services

Target Market(s)

photography

Industry/Entity Type

Photographer

Coding

Coded - Design and coding required

Number of Pages Required

5+ page

Colors

Designer to choose colors to be used in the design.

Requirements
Must have
• clean eye catching elegant trendy
Nice to have
• unique and creative from other photographer websites

```html
<!DOCTYPE html>
<html lang="en">
<head>
<meta charset="utf-8">
<title>Northern Horizons — Photography</title>
<link rel="stylesheet" href="https://fonts.googleapis.com/css2?family=Poppins:wght@300;400;500;600;700&display=swap">
<style>
:root{
  --ink:#1c1c1c;
  --dark:#2b2b2b;
  --muted:#777;
  --faint:#ececec;
  --soft-bg:#f6f6f6;
  --white:#ffffff;
  --accent:#ffe600;
  --link:#2a7de1;
}
*{box-sizing:border-box;margin:0;padding:0}
html,body{width:1200px;height:2952px;overflow:hidden}
body{font-family:'Poppins',sans-serif;color:var(--ink);background:var(--white);position:relative}
.abs{position:absolute}

/* nav */
.site-nav{left:0;top:0;width:1200px;height:60px;background:var(--white)}
.logo{left:88px;top:18px;font-weight:700;font-size:19px;letter-spacing:1px}
.menu{left:272px;top:0;display:flex;gap:46px;height:60px;align-items:center;font-size:12px;font-weight:500;letter-spacing:.5px}
.menu a{color:var(--ink);text-decoration:none;position:relative;padding:6px 0}
.menu a.active::after{content:"";position:absolute;left:0;right:0;bottom:0;height:3px;background:var(--accent)}
.nav-phone{left:1010px;top:0;width:190px;height:60px;background:var(--dark);color:var(--white);font-size:13px;display:flex;align-items:center;justify-content:center;letter-spacing:.5px}

/* hero */
.hero-photo{left:0;top:60px;width:1070px;height:580px;background:linear-gradient(100deg,#b59a78 0%,#9fb8c9 35%,#6ea6c8 60%,#4c87a8 80%,#cbb595 100%)}
.hero-card{left:80px;top:140px;width:692px;height:260px;background:rgba(255,255,255,.35)}
.hero-kicker{left:130px;top:178px;font-size:13px;letter-spacing:1px;color:var(--ink)}
.hero-rule{left:90px;top:224px;width:90px;height:2px;background:var(--ink)}
.hero-title{left:216px;top:190px;font-size:58px;font-weight:500;color:var(--ink)}
.hero-place{left:130px;top:280px;font-size:13px;display:flex;align-items:center;gap:8px}
.btn-detail{left:130px;top:324px;width:100px;height:34px;background:var(--accent);border-radius:17px;font-size:11px;font-weight:600;display:flex;align-items:center;justify-content:center;letter-spacing:1px}
.scroll-col{left:1070px;top:60px;width:130px;height:500px;background:var(--white)}
.scroll-text{left:1120px;top:120px;writing-mode:vertical-rl;font-size:13px;letter-spacing:5px}
.scroll-arrow{left:1128px;top:390px}
.hero-social{left:0;top:580px;width:280px;height:60px;background:var(--white);display:flex;align-items:center;gap:22px;padding-left:30px}
.social-dot{width:14px;height:14px;background:var(--ink);border-radius:3px}
.slider-ctrl{left:944px;top:560px;width:256px;height:80px;display:flex}
.slider-ctrl div{flex:1;display:flex;align-items:center;justify-content:center}
.slider-prev{background:#555}
.slider-next{background:var(--dark)}

/* category */
.category{left:0;top:640px;width:1200px;height:560px;background:var(--soft-bg)}
.ghost{font-weight:700;color:var(--faint);letter-spacing:10px;text-align:center;width:1200px;left:0}
.section-title{width:1200px;left:0;text-align:center;font-size:17px;font-weight:600;letter-spacing:1px}
.cat-card{top:820px;width:222px;height:240px;border-radius:6px;display:flex;align-items:center;justify-content:center;color:var(--white);font-size:14px;font-weight:600;letter-spacing:2px}
.more-link{width:1200px;left:0;text-align:center;font-size:13px;font-weight:500;letter-spacing:1px;display:flex;justify-content:center;align-items:center;gap:10px}

/* gallery */
.tile{border-radius:6px}

/* about */
.about{left:0;top:2320px;width:600px;height:520px;background:var(--soft-bg)}
.about-photo{left:600px;top:2320px;width:600px;height:520px;background:linear-gradient(180deg,#3d5170 0%,#7a8aa3 45%,#c9a27f 65%,#3a3f4a 100%)}
.about-ghost{left:60px;top:2380px;font-size:120px;font-weight:700;color:#e4e4e4;letter-spacing:6px}
.about-title{left:88px;top:2420px;font-size:60px;font-weight:500}
.about-text{left:88px;top:2520px;width:430px;font-size:14px;line-height:24px;color:#444}
.about-cta{left:88px;top:2684px;font-size:14px}
.about-cta b{color:var(--link)}
.about-social{left:88px;top:2728px;display:flex;gap:22px}

/* footer */
.site-footer{left:0;top:2840px;width:1200px;height:112px;background:var(--accent);display:flex;align-items:center;justify-content:center;font-size:14px;font-weight:500;gap:10px}
</style>
</head>
<body>

<header class="abs site-nav">
  <div class="abs logo">LOGO</div>
  <nav class="abs menu">
    <a class="active" href="#">HOME</a><a href="#">GALLRY</a><a href="#">MY BIO</a><a href="#">ABOUT ME</a><a href="#">CONTACT</a>
  </nav>
  <div class="abs nav-phone">+00 123 456 78</div>
</header>

<section>
  <div class="abs hero-photo" role="img" aria-label="Coastal beach with rocky cliff and blue sea"></div>
  <div class="abs hero-card"></div>
  <div class="abs hero-kicker">SANTANA BEACH</div>
  <div class="abs hero-rule"></div>
  <h1 class="abs hero-title">Santana Beach</h1>
  <div class="abs hero-place">
    <svg width="12" height="16" viewBox="0 0 12 16"><path d="M6 0a6 6 0 0 0-6 6c0 4.5 6 10 6 10s6-5.5 6-10a6 6 0 0 0-6-6zm0 8.5A2.5 2.5 0 1 1 6 3.5a2.5 2.5 0 0 1 0 5z" fill="#1c1c1c"/></svg>
    Located in the Sandbar
  </div>
  <div class="abs btn-detail">DETAIL</div>
  <div class="abs scroll-col"></div>
  <div class="abs scroll-text">SCROLL DOWN</div>
  <svg class="abs scroll-arrow" width="14" height="30" viewBox="0 0 14 30"><path d="M7 0v28M1 22l6 6 6-6" stroke="#1c1c1c" stroke-width="2" fill="none"/></svg>
  <div class="abs hero-social"><span class="social-dot"></span><span class="social-dot"></span><span class="social-dot"></span><span class="social-dot"></span></div>
  <div class="abs slider-ctrl">
    <div class="slider-prev"><svg width="40" height="16" viewBox="0 0 40 16"><path d="M40 8H2M9 1 2 8l7 7" stroke="#ccc" stroke-width="2" fill="none"/></svg></div>
    <div class="slider-next"><svg width="40" height="16" viewBox="0 0 40 16"><path d="M0 8h38M31 1l7 7-7 7" stroke="#fff" stroke-width="2" fill="none"/></svg></div>
  </div>
</section>

<section>
  <div class="abs category"></div>
  <div class="abs ghost" style="top:662px;font-size:90px">CATEGORY</div>
  <h2 class="abs section-title" style="top:710px">CHOOSE YOU WANT TO SEE</h2>
  <div class="abs cat-card" style="left:128px;background:linear-gradient(160deg,#8a97a8,#3f4a58)" role="img" aria-label="Snowy mountain peak">NATURE</div>
  <div class="abs cat-card" style="left:368px;background:linear-gradient(160deg,#d8864a,#2f3c4c)" role="img" aria-label="Town buildings against sky">TOWN</div>
  <div class="abs cat-card" style="left:608px;background:linear-gradient(160deg,#c9c06a,#5d6a48)" role="img" aria-label="Sliced lemons and herbs">FOOD</div>
  <div class="abs cat-card" style="left:848px;background:linear-gradient(160deg,#a6b6c4,#8a4a3a)" role="img" aria-label="Colourful city houses">CITIES</div>
  <div class="abs more-link" style="top:1100px">OTHER <svg width="18" height="10" viewBox="0 0 18 10"><path d="M0 5h16M12 1l4 4-4 4" stroke="#1c1c1c" stroke-width="1.5" fill="none"/></svg></div>
</section>

<section>
  <div class="abs ghost" style="top:1222px;font-size:90px">GALLERY</div>
  <h2 class="abs section-title" style="top:1244px">GALLERY</h2>
  <div class="abs tile" style="left:128px;top:1360px;width:304px;height:224px;background:linear-gradient(180deg,#2d6fb8,#8fb8dc)" role="img" aria-label="Glass skyscraper against blue sky"></div>
  <div class="abs tile" style="left:128px;top:1608px;width:304px;height:260px;background:linear-gradient(180deg,#2a8fc4,#0f3f66)" role="img" aria-label="Diver under blue water"></div>
  <div class="abs tile" style="left:128px;top:1888px;width:304px;height:300px;background:linear-gradient(180deg,#c9b9a2,#6c7480)" role="img" aria-label="Misty mountains above clouds"></div>
  <div class="abs tile" style="left:448px;top:1360px;width:304px;height:400px;background:linear-gradient(180deg,#cfcfcf,#b8b8b8)" role="img" aria-label="Red white and blue ice pop"></div>
  <div class="abs tile" style="left:448px;top:1784px;width:304px;height:276px;background:linear-gradient(180deg,#8a5a34,#3a2618)" role="img" aria-label="Library interior with bookshelves"></div>
  <div class="abs tile" style="left:768px;top:1360px;width:304px;height:312px;background:linear-gradient(180deg,#e8e2d8,#8a7a64)" role="img" aria-label="Meeting room with chairs and windows"></div>
  <div class="abs tile" style="left:768px;top:1696px;width:304px;height:328px;background:linear-gradient(180deg,#2c2a1e,#b8572a 55%,#5c7a2c)" role="img" aria-label="Orange mushrooms on moss"></div>
  <div class="abs more-link" style="top:2240px">LOAD MORE <svg width="18" height="10" viewBox="0 0 18 10"><path d="M0 5h16M12 1l4 4-4 4" stroke="#1c1c1c" stroke-width="1.5" fill="none"/></svg></div>
</section>

<section>
  <div class="abs about"></div>
  <div class="abs about-photo" role="img" aria-label="Person working on laptop above city at dusk"></div>
  <div class="abs about-ghost">ABOUT</div>
  <h2 class="abs about-title">About Me</h2>
  <p class="abs about-text">Lorem ipsum dolor sit amet, consectetur adipisicing elit, sed do eiusmod tempor incididunt ut labore et dolore magna aliqua. Ut enim ad minim veniam, quis nostrud exercitation ullamco laboris nisi ut aliquip ex ea commodo consequat.</p>
  <p class="abs about-cta">Interest work with me <b>Lets Talk</b></p>
  <div class="abs about-social"><span class="social-dot"></span><span class="social-dot"></span><span class="social-dot"></span><span class="social-dot"></span></div>
</section>

<footer class="abs site-footer">
  <svg width="16" height="16" viewBox="0 0 16 16"><circle cx="8" cy="8" r="7" stroke="#1c1c1c" stroke-width="1.5" fill="none"/><path d="M10.5 6a3 3 0 1 0 0 4" stroke="#1c1c1c" stroke-width="1.5" fill="none"/></svg>
  Copyright 2019, All Reserved
</footer>

</body>
</html>
```